National Female Non-profit Business Card

We need a business card design as soon as possible for a non-profit organisation called Meadow to Summit. Our aim is to empower leadership potential in rural female teens.
The business card should have our logo on the one side and then information on the other side, including name, job title, email address, phone number and website (www.meadowtosummit.com.au) and our twitter handle @MeadowSummit
It should use the colours white, coral (#f04a50) and orange (#f68e4e). The font used in the logo is Raleway.
The hashtag #YoungVoicesRise could be used.
It should be bright, chic and crisp. Our logo is attached.

Target Market(s)
We will be handing the cards out to politicians and senior executives. However, as we're a non-profit for young women, they also need to reflect femininity and youth.
Industry/Entity Type
Non-Profit
Look and feel

```html
<!DOCTYPE html>
<html lang="en">
<head>
<meta charset="utf-8">
<title>Meadow to Summit – Business Card</title>
<link href="https://fonts.googleapis.com/css2?family=Lato:wght@400;700;900&family=Raleway:wght@300;400&display=swap" rel="stylesheet">
<style>
  :root{
    --coral:#f04a50;
    --coral-deep:#e63f47;
    --orange:#f68e4e;
    --ink:#1e1e1e;
    --paper:#ffffff;
    --paper-shade:#ececec;
    --backdrop:#2a2a2a;
  }
  *{margin:0;padding:0;box-sizing:border-box}
  html,body{width:1200px;height:997px;overflow:hidden;background:var(--backdrop)}
  .canvas{position:relative;width:1200px;height:997px}
  .card{position:absolute;left:250px;width:700px;height:400px;border-radius:26px;overflow:hidden}
  .card--front{top:72px;background:linear-gradient(135deg,#f2575c 0%,var(--coral) 45%,var(--coral-deep) 100%)}
  .card--back{top:525px;background:linear-gradient(135deg,var(--paper) 0%,#f7f7f7 55%,var(--paper-shade) 100%)}

  .front-mark{position:absolute;left:0;right:0;top:170px;display:flex;justify-content:center;align-items:center;gap:16px}
  .front-mark__dot{width:22px;height:22px;border-radius:50%;background:var(--paper)}
  .front-mark__name{font-family:"Raleway",sans-serif;font-weight:300;font-size:40px;letter-spacing:2px;color:var(--paper)}

  .back-mark{position:absolute;left:0;right:0;top:42px;text-align:center}
  .back-mark__name{display:inline-flex;align-items:center;gap:10px;font-family:"Raleway",sans-serif;font-weight:400;font-size:22px;letter-spacing:1px;color:var(--coral)}
  .back-mark__dot{width:12px;height:12px;border-radius:50%;background:var(--coral)}
  .back-mark__web{display:flex;justify-content:center;align-items:center;gap:14px;margin-top:6px;font-family:"Lato",sans-serif;font-weight:900;font-size:15px;color:var(--ink)}
  .back-mark__rule{width:48px;height:3px;background:var(--coral)}

  .person{position:absolute;left:62px;top:168px;font-family:"Lato",sans-serif}
  .person__name{font-weight:900;font-size:26px;color:var(--orange);letter-spacing:.5px}
  .person__role{font-weight:900;font-size:15px;color:var(--ink);margin-top:2px}

  .socials{position:absolute;left:62px;top:262px;list-style:none;font-family:"Lato",sans-serif;font-size:17px;font-weight:700;font-style:normal;color:var(--ink)}
  .socials li{display:flex;align-items:center;gap:12px;height:36px}
  .bullet{width:24px;height:24px;border-radius:50%;background:var(--orange);flex:none;display:flex;align-items:center;justify-content:center}

  .divider{position:absolute;left:340px;top:158px;width:3px;height:200px;background:linear-gradient(to bottom,rgba(246,142,78,.15),var(--orange) 40%,rgba(246,142,78,.1))}

  .contacts{position:absolute;left:372px;top:164px;list-style:none;font-family:"Lato",sans-serif;font-size:16px;font-weight:700;color:var(--ink)}
  .contacts li{display:flex;align-items:center;gap:12px;height:36px}
</style>
</head>
<body>
<main class="canvas">

  <section class="card card--front" aria-label="Card front">
    <div class="front-mark">
      <span class="front-mark__dot"></span>
      <span class="front-mark__name">MEADOW TO SUMMIT</span>
    </div>
  </section>

  <section class="card card--back" aria-label="Card back">
    <header class="back-mark">
      <div class="back-mark__name"><span class="back-mark__dot"></span>MEADOW TO SUMMIT</div>
      <div class="back-mark__web"><span class="back-mark__rule"></span>www.meadowtosummit.com.au<span class="back-mark__rule"></span></div>
    </header>

    <div class="person">
      <p class="person__name">MAYA HOLLIS</p>
      <p class="person__role">OWNER / FOUNDER</p>
    </div>

    <ul class="socials">
      <li><span class="bullet"></span>/MeadowtoSummit</li>
      <li><span class="bullet"></span>/MeadowSummit</li>
      <li><span class="bullet"></span>/Meadow_to_Summit</li>
    </ul>

    <div class="divider"></div>

    <ul class="contacts">
      <li><span class="bullet"><svg width="14" height="14" viewBox="0 0 24 24" fill="#fff"><path d="M6.6 10.8a15 15 0 0 0 6.6 6.6l2.2-2.2c.3-.3.7-.4 1-.2 1.1.4 2.3.6 3.6.6.6 0 1 .4 1 1V20c0 .6-.4 1-1 1A17 17 0 0 1 3 4c0-.6.4-1 1-1h3.5c.6 0 1 .4 1 1 0 1.3.2 2.5.6 3.6.1.3 0 .7-.2 1z"/></svg></span>0400 512 730</li>
      <li><span class="bullet"><svg width="14" height="14" viewBox="0 0 24 24" fill="#fff"><path d="M6.6 10.8a15 15 0 0 0 6.6 6.6l2.2-2.2c.3-.3.7-.4 1-.2 1.1.4 2.3.6 3.6.6.6 0 1 .4 1 1V20c0 .6-.4 1-1 1A17 17 0 0 1 3 4c0-.6.4-1 1-1h3.5c.6 0 1 .4 1 1 0 1.3.2 2.5.6 3.6.1.3 0 .7-.2 1z"/></svg></span>0400 512 846</li>
      <li><span class="bullet"><svg width="14" height="14" viewBox="0 0 24 24" fill="none" stroke="#fff" stroke-width="2.4"><rect x="3" y="6" width="18" height="12" rx="1"/><path d="M3 7l9 6 9-6"/></svg></span>contact@meadowtosummit.com.au</li>
      <li><span class="bullet"><svg width="14" height="14" viewBox="0 0 24 24" fill="#fff"><path d="M12 2a7 7 0 0 0-7 7c0 5 7 13 7 13s7-8 7-13a7 7 0 0 0-7-7zm0 9.5A2.5 2.5 0 1 1 12 6.5a2.5 2.5 0 0 1 0 5z"/></svg></span>12/8 Wattle Lane, Hillview NSW 2999</li>
    </ul>
  </section>

</main>
</body>
</html>
```